At Home Pet Euthanasia - business cards & brand stationary

We already have a logo and the colors and a website. Need a business card designed that will be able to customized to multiple veterinarians who will be partnering with us. The feel needs to be compassionate, comforting with our tagline 'A Gift of Love at Home'. It will be 2 sides.
On the back our platform/partner vets will be customizing each business card with their own service areas, phone numbers, name and title. On the front, i would like to see experimentation with use of our photos, the logo, tagline and a description 'Peaceful and Compassionate At-Home Pet Euthanasia'

```html
<!DOCTYPE html>
<html lang="en">
<head>
<meta charset="utf-8">
<title>Hearthpaw Business Card</title>
<link rel="stylesheet" href="https://fonts.googleapis.com/css2?family=Montserrat:wght@400;600&family=Raleway:ital,wght@1,300&display=swap">
<style>
  :root {
    --backdrop: #cccccc;
    --paper: #ffffff;
    --brand-blue: #7699c0;
    --photo-light: #dbe5f0;
    --photo-mid: #a9bfd9;
    --ink: #333333;
  }
  * { margin: 0; padding: 0; box-sizing: border-box; }
  html, body {
    width: 1000px;
    height: 1200px;
    overflow: hidden;
    background: var(--backdrop);
  }
  .card {
    position: absolute;
    left: 51px;
    width: 898px;
    height: 538px;
    background: var(--paper);
    overflow: hidden;
  }
  .card--front { top: 44px; }
  .card--back { top: 617px; }
  .card__waves {
    position: absolute;
    inset: 0;
    width: 898px;
    height: 538px;
  }
  .card__waves path { fill: var(--brand-blue); }

  .brand-mark {
    position: absolute;
    border-radius: 50%;
  }
  .card--front .brand-mark {
    left: 190px;
    top: 80px;
    width: 100px;
    height: 100px;
    background: var(--brand-blue);
  }
  .brand-name {
    position: absolute;
    font-family: "Montserrat", sans-serif;
    font-weight: 600;
    letter-spacing: -1px;
    line-height: 1;
    white-space: nowrap;
  }
  .card--front .brand-name {
    left: 240px;
    top: 205px;
    transform: translateX(-50%);
    font-size: 58px;
    color: var(--brand-blue);
  }

  .photo-slot {
    position: absolute;
    left: 78px;
    top: 292px;
    width: 324px;
    height: 216px;
    border-radius: 14px;
    background: linear-gradient(120deg, var(--photo-mid) 0%, var(--photo-light) 55%, var(--photo-mid) 100%);
  }

  .contact {
    position: absolute;
    left: 557px;
    top: 256px;
    font-family: "Montserrat", sans-serif;
    color: var(--ink);
  }
  .contact__name {
    font-size: 25px;
    font-weight: 600;
    line-height: 30px;
  }
  .contact__title {
    font-size: 23px;
    font-weight: 400;
    line-height: 30px;
    margin-bottom: 14px;
  }
  .contact__list { list-style: none; }
  .contact__item {
    display: flex;
    align-items: center;
    height: 38.5px;
    font-size: 21.5px;
  }
  .contact__icon {
    width: 23px;
    height: 23px;
    margin-right: 10px;
    flex: none;
    background: var(--brand-blue);
    border-radius: 3px;
  }
  .contact__icon svg { display: block; width: 23px; height: 23px; }
  .contact__icon path, .contact__icon circle, .contact__icon rect, .contact__icon line {
    fill: none;
    stroke: var(--paper);
    stroke-width: 1.5;
    stroke-linecap: round;
    stroke-linejoin: round;
  }

  .card--back .brand-lockup {
    position: absolute;
    left: 0;
    right: 0;
    top: 225px;
    display: flex;
    align-items: center;
    justify-content: center;
    gap: 22px;
  }
  .card--back .brand-mark {
    position: static;
    width: 96px;
    height: 96px;
    background: var(--paper);
  }
  .card--back .brand-name {
    position: static;
    font-size: 78px;
    color: var(--paper);
  }
  .tagline {
    position: absolute;
    left: 0;
    right: 0;
    top: 390px;
    text-align: center;
    font-family: "Raleway", sans-serif;
    font-style: italic;
    font-weight: 300;
    font-size: 44px;
    color: var(--paper);
  }
</style>
</head>
<body>

<section class="card card--front">
  <svg class="card__waves" viewBox="0 0 898 538" aria-hidden="true">
    <path d="M0 0 H898 V64 C830 92 720 90 580 68 C430 42 260 12 0 64 Z"/>
    <path d="M0 474 C130 440 260 470 420 500 C600 532 770 520 898 474 V538 H0 Z"/>
  </svg>

  <div class="brand-mark" aria-hidden="true"></div>
  <div class="brand-name">Hearthpaw</div>

  <div class="photo-slot" role="img" aria-label="Photo of a child gently holding a pet cat"></div>

  <div class="contact">
    <p class="contact__name">Your Name</p>
    <p class="contact__title">Manager</p>
    <ul class="contact__list">
      <li class="contact__item">
        <span class="contact__icon"><svg viewBox="0 0 23 23" aria-hidden="true"><path d="M7 5 L9.5 5 L10.5 8.5 L9 9.8 C9.8 11.8 11.2 13.2 13.2 14 L14.5 12.5 L18 13.5 L18 16 C18 17 17 18 16 18 C10.5 17.5 5.5 12.5 5 7 C5 6 6 5 7 5 Z"/></svg></span>
        123 444 555
      </li>
      <li class="contact__item">
        <span class="contact__icon"><svg viewBox="0 0 23 23" aria-hidden="true"><path d="M11.5 18.5 C8 14 7 12 7 9.5 A4.5 4.5 0 0 1 16 9.5 C16 12 15 14 11.5 18.5 Z"/><circle cx="11.5" cy="9.5" r="1.6"/></svg></span>
        789 Your Street Here
      </li>
      <li class="contact__item">
        <span class="contact__icon"><svg viewBox="0 0 23 23" aria-hidden="true"><rect x="4.5" y="6.5" width="14" height="10" rx="1"/><path d="M4.5 7 L11.5 12.5 L18.5 7"/></svg></span>
        info@yourname.com
      </li>
      <li class="contact__item">
        <span class="contact__icon"><svg viewBox="0 0 23 23" aria-hidden="true"><circle cx="11.5" cy="11.5" r="6.5"/><line x1="5" y1="11.5" x2="18" y2="11.5"/><path d="M11.5 5 C8.8 8 8.8 15 11.5 18 C14.2 15 14.2 8 11.5 5 Z"/></svg></span>
        www.yourname.com
      </li>
    </ul>
  </div>
</section>

<section class="card card--back">
  <svg class="card__waves" viewBox="0 0 898 538" aria-hidden="true">
    <path d="M0 64 C60 88 160 92 300 72 C430 52 530 20 650 22 C760 24 840 44 898 64 V474 C820 452 720 455 580 478 C420 504 260 518 120 500 C60 492 20 482 0 474 Z"/>
  </svg>

  <div class="brand-lockup">
    <div class="brand-mark" aria-hidden="true"></div>
    <div class="brand-name">Hearthpaw</div>
  </div>

  <p class="tagline">Gentle care, close to home.</p>
</section>

</body>
</html>
```